Webpage for a treatment housing for young addicts.

I need a new design and files for my wordpress page. I need it to be more neat and clean. I need it to look professional with a starting page that will work as a navigation. I need like logo and phone number and such up top, a picture under it with one sentence as a slogan and under it 6 boxes to click to come to our different pages. Under it I want news etc.

Target Market(s)

Social services, employees and governements

Coding

Coded - Design and coding required

Font styles to use
Sans Serif

Colors
abd037
3176b5
9d9d9d
aaaaaa
f04a50

Requirements
Must have
• A nice design
Nice to have
• need it to look professional with a starting page that will work as a navigation. I need like logo and phone number and such up top, a picture under it with one sentence as a slogan and under it 6 boxes to click to come to our different pages. Under it I want news etc.
• today www.kelmora.se
• want more like www.trivest.se or www.solbrink.se
Should not have
• To many different colours and a messy design.

```html
<!DOCTYPE html>
<html lang="en">
<head>
<meta charset="utf-8">
<title>Kelmora – Home</title>
<link href="https://fonts.googleapis.com/css2?family=Raleway:wght@400;500;600&family=Open+Sans:wght@400;600&display=swap" rel="stylesheet">
<style>
:root{
  --green:#84c441;
  --blue:#1a8bd2;
  --dark:#222;
  --text:#555;
  --muted:#777;
  --line:#ddd;
  --panel:#f3f3f3;
  --white:#fff;
}
*{box-sizing:border-box;margin:0;padding:0}
html,body{width:1200px;height:2917px;overflow:hidden}
body{position:relative;background:var(--white);font-family:"Open Sans",Arial,sans-serif;color:var(--text)}
.abs{position:absolute}
.topline{left:0;top:0;width:1200px;height:4px;background:var(--green)}
.header{left:0;top:4px;width:1200px;height:89px;background:var(--white)}
.brand{left:78px;top:24px;display:flex;align-items:center;gap:10px}
.brand-dot{width:40px;height:40px;border-radius:50%;background:var(--green)}
.brand-name{font-family:"Raleway",sans-serif;font-weight:600;font-size:28px;color:var(--blue)}
.nav{left:364px;top:0;height:89px;display:flex;align-items:center;font-family:"Raleway",sans-serif;font-size:14px;font-weight:500;color:#333}
.nav a{text-decoration:none;color:inherit;padding:0 15px;height:89px;display:flex;align-items:center;text-transform:uppercase}
.nav a.active{background:var(--green);color:var(--white);padding:0 18px}
.nav-phone{left:990px;top:0;height:89px;display:flex;align-items:center;gap:10px;border-left:1px solid var(--line);padding-left:22px;font-size:14px;color:#333}
.hero{left:0;top:93px;width:1200px;height:563px;background:linear-gradient(160deg,#b7c08a 0%,#5d7a3a 35%,#7a5432 70%,#c9a27a 100%)}
.slogan{left:747px;top:198px;width:362px;height:362px;border-radius:50%;background:var(--blue);display:flex;align-items:center;justify-content:center;text-align:center;font-family:"Raleway",sans-serif;font-size:31px;line-height:1.35;color:var(--white);padding:40px}
.hero-next{left:1032px;top:476px;width:56px;height:56px;border-radius:50%;background:#333}
.tiles{left:0;top:656px;width:1200px;height:385px;background:var(--panel)}
.tile{width:332px;height:103px;background:var(--white);box-shadow:0 2px 8px rgba(0,0,0,.08);display:flex;align-items:center;justify-content:center;font-size:17px;color:#555}
.welcome-photo{left:78px;top:1124px;width:665px;height:459px;background:linear-gradient(150deg,#dfe1dc 0%,#5f7d3e 40%,#8a6a42 65%,#b7ad8f 100%)}
.welcome-card{left:613px;top:1167px;width:509px;height:373px;background:var(--white);box-shadow:0 2px 14px rgba(0,0,0,.12);padding:56px 36px}
h1,h2{font-family:"Raleway",sans-serif;font-weight:400;color:var(--dark)}
.welcome-card h1{font-size:40px;margin-bottom:18px}
.welcome-card p{font-size:13.5px;line-height:25px;color:#555}
.btn{display:inline-block;margin-top:20px;background:var(--blue);color:var(--white);font-family:"Raleway",sans-serif;font-weight:600;font-size:17px;width:186px;height:46px;line-height:46px;text-align:center}
.about{left:0;top:1667px;width:1200px;height:447px;background:var(--panel);text-align:center}
.about h2{position:absolute;top:52px;width:100%;font-size:38px}
.about p{position:absolute;top:112px;left:150px;width:900px;font-size:13.5px;line-height:26px}
.value{width:280px;text-align:center}
.value-ring{width:140px;height:140px;margin:0 auto;border-radius:50%;border:2px solid #8bb9dc;padding:7px}
.value-ring div{width:100%;height:100%;border-radius:50%;background:var(--white);border:1px solid #cfdde8;display:flex;align-items:center;justify-content:center}
.value h3{margin-top:22px;font-family:"Raleway",sans-serif;font-weight:500;font-size:20px;color:#333}
.news h2{left:0;top:2158px;width:1200px;text-align:center;font-size:38px}
.post{top:2229px;width:323px;height:228px;background:var(--white);box-shadow:0 2px 10px rgba(0,0,0,.12);padding:40px 14px 0}
.post h3{font-family:"Raleway",sans-serif;font-weight:500;font-size:23px;color:#333;margin-bottom:10px}
.post p{font-size:14px;line-height:25px;color:#555;padding-bottom:14px;border-bottom:1px solid var(--line)}
.post-meta{display:flex;justify-content:space-between;align-items:center;font-size:13.5px;margin-top:14px}
.post-meta span{display:flex;align-items:center;gap:8px}
.newsletter{left:0;top:2542px;width:1200px;height:311px;background:var(--panel)}
.newsletter-title{left:0;top:2598px;width:1200px;text-align:center;font-family:"Raleway",sans-serif;font-size:18px;color:#444}
.signup{left:344px;top:2641px;width:508px;height:45px;border:1px solid #ccc;border-radius:23px;background:var(--white);display:flex;align-items:center;justify-content:space-between;padding-left:22px;font-size:13px;color:#666}
.signup b{font-weight:400;background:var(--green);color:#222;height:43px;width:170px;border-radius:22px;display:flex;align-items:center;justify-content:center;font-family:"Raleway",sans-serif;font-size:19px}
.foot-col{top:2742px;font-size:13.5px;line-height:28px;color:#444;text-align:center}
.divider{top:2748px;width:1px;height:56px;background:#ccc}
.social{top:2738px;width:57px;height:57px;border-radius:50%;background:var(--green)}
.copyright{left:0;top:2853px;width:1200px;height:64px;background:var(--green);display:flex;align-items:center;justify-content:center;font-size:13px;color:#2d3d1a}
</style>
</head>
<body>
<div class="abs topline"></div>
<header class="abs header">
  <div class="abs brand"><span class="brand-dot"></span><span class="brand-name">Kelmora</span></div>
  <nav class="abs nav">
    <a class="active" href="#">Home</a><a href="#">About Kelmora</a><a href="#">Björkgården HVB</a><a href="#">Work with us</a><a href="#">News</a><a href="#">Plug</a>
  </nav>
  <div class="abs nav-phone">
    <svg width="20" height="20" viewBox="0 0 24 24"><path fill="#84c441" d="M6.6 10.8a15 15 0 006.6 6.6l2.2-2.2c.3-.3.7-.4 1-.2 1.1.4 2.3.6 3.6.6.6 0 1 .4 1 1V20c0 .6-.4 1-1 1A17 17 0 013 4c0-.6.4-1 1-1h3.5c.6 0 1 .4 1 1 0 1.3.2 2.5.6 3.6.1.3 0 .7-.2 1z"/></svg>
    010-4827315
  </div>
</header>

<section class="abs hero" role="img" aria-label="Garden path seen from a wooden veranda with lush green plants"></section>
<div class="abs slogan">"We Create Sustainable Roads to a Better Future"</div>
<div class="abs hero-next"><svg width="56" height="56" viewBox="0 0 56 56"><path d="M19 28h18M30 21l7 7-7 7" stroke="#fff" stroke-width="3" fill="none" stroke-linecap="round" stroke-linejoin="round"/></svg></div>

<section class="abs tiles"></section>
<a class="abs tile" style="left:78px;top:731px">Therapeutic Environment The</a>
<a class="abs tile" style="left:434px;top:731px">The starting point of the treatment</a>
<a class="abs tile" style="left:790px;top:731px">Individually tailored</a>
<a class="abs tile" style="left:78px;top:856px">Active contact person</a>
<a class="abs tile" style="left:434px;top:856px">Measuring The</a>
<a class="abs tile" style="left:790px;top:856px">Salutogenic perspective</a>

<div class="abs welcome-photo" role="img" aria-label="White house entrance with wooden door framed by climbing plants and flowers"></div>
<section class="abs welcome-card">
  <h1>WELCOME TO KELMORA</h1>
  <p>Kelmora Sverige AB carries out care and care aimed at people aged 14-25 years. This is done primarily through Home for care and housing (HVB) . We are specialists in psychosocial abuse and crime issues. By being constantly open to new methods and aware of the existing ones, we develop and improve our care.</p>
  <a class="btn">KNOW MORE</a>
</section>

<section class="abs about">
  <h2>ABOUT KELMORA</h2>
  <p>We want to create a therapeutic treatment environment through evidence-based methods, high skills and combined experience. We want every individual to have the opportunity to change and influence his own situation for a better and more well functioning.</p>
</section>
<div class="abs value" style="left:99px;top:1856px">
  <div class="value-ring"><div><svg width="64" height="48" viewBox="0 0 64 48" fill="none" stroke="#1a8bd2" stroke-width="2"><circle cx="14" cy="10" r="5"/><circle cx="32" cy="10" r="5"/><circle cx="50" cy="10" r="5"/><path d="M6 28v-6a8 8 0 0116 0v6M24 28v-6a8 8 0 0116 0v6M42 28v-6a8 8 0 0116 0v6M2 30h60v6H2zM10 36v10M54 36v10"/></svg></div></div>
  <h3>The team</h3>
</div>
<div class="abs value" style="left:463px;top:1856px">
  <div class="value-ring"><div><svg width="44" height="60" viewBox="0 0 44 60" fill="none" stroke="#1a8bd2" stroke-width="2"><circle cx="22" cy="22" r="18"/><circle cx="22" cy="22" r="10"/><circle cx="22" cy="22" r="4"/><path d="M12 37l-6 20 8-4 4 6 4-18M32 37l6 20-8-4-4 6"/></svg></div></div>
  <h3>Quality work</h3>
</div>
<div class="abs value" style="left:823px;top:1856px">
  <div class="value-ring"><div><svg width="62" height="50" viewBox="0 0 62 50" fill="none" stroke="#1a8bd2" stroke-width="2" stroke-linejoin="round"><path d="M14 4h34l12 14-29 28L2 18zM2 18h58M20 4l-6 14 17 28 17-28-6-14M31 4l-11 14M31 4l11 14"/></svg></div></div>
  <h3>Value base &amp; ethical appoach</h3>
</div>

<section class="news">
  <h2 class="abs news-title" style="left:0;top:2158px;width:1200px;text-align:center;font-size:38px">LATEST NEWS</h2>
  <article class="abs post" style="left:78px">
    <h3>Blog Title</h3>
    <p>Lorem Ipsum is simply dummy text of the printing and typesetting industry.</p>
    <div class="post-meta"><span>by admin</span><span><svg width="20" height="18" viewBox="0 0 20 18" fill="none" stroke="#666" stroke-width="1.5"><rect x="1" y="3" width="18" height="14"/><path d="M1 7h18M5 1v4M15 1v4M5 10h2M9 10h2M13 10h2M5 13h2M9 13h2"/></svg>12th April 2018</span></div>
  </article>
  <article class="abs post" style="left:438px">
    <h3>Blog Title</h3>
    <p>Lorem Ipsum is simply dummy text of the printing and typesetting industry.</p>
    <div class="post-meta"><span>by admin</span><span><svg width="20" height="18" viewBox="0 0 20 18" fill="none" stroke="#666" stroke-width="1.5"><rect x="1" y="3" width="18" height="14"/><path d="M1 7h18M5 1v4M15 1v4M5 10h2M9 10h2M13 10h2M5 13h2M9 13h2"/></svg>12th April 2018</span></div>
  </article>
  <article class="abs post" style="left:801px">
    <h3>Blog Title</h3>
    <p>Lorem Ipsum is simply dummy text of the printing and typesetting industry.</p>
    <div class="post-meta"><span>by admin</span><span><svg width="20" height="18" viewBox="0 0 20 18" fill="none" stroke="#666" stroke-width="1.5"><rect x="1" y="3" width="18" height="14"/><path d="M1 7h18M5 1v4M15 1v4M5 10h2M9 10h2M13 10h2M5 13h2M9 13h2"/></svg>12th April 2018</span></div>
  </article>
</section>

<footer>
  <div class="abs newsletter"></div>
  <div class="abs newsletter-title">Subscribe to our newsletter</div>
  <div class="abs signup">Enter your email<b>SUBSCRIBE</b></div>
  <div class="abs foot-col" style="left:130px;width:240px">Kelmora Sverige AB<br>Lindvägen 12 268 40 Ekby</div>
  <div class="abs divider" style="left:420px"></div>
  <a class="abs social" style="left:501px" aria-label="Social link"></a>
  <a class="abs social" style="left:571px" aria-label="Social link"></a>
  <a class="abs social" style="left:641px" aria-label="Social link"></a>
  <div class="abs divider" style="left:782px"></div>
  <div class="abs foot-col" style="left:840px;width:240px;text-align:center">CALL US : 010-4827315<br>EMAIL US : info@kelmora.se</div>
  <div class="abs copyright">©Kelmora- 2018. All Rights Reserved.</div>
</footer>
</body>
</html>
```